Birch & Ember Website Design (Rustic/Western)

OVERVIEW
Birch & Ember Supply House (aka Birch & Ember) manufactures rustic / western furniture and décor for cabins, lodges, and ranches. We also offer a line of accessories to complement our product line.
WEB PAGE (www.BirchAndEmber.example)
We are looking for a new web page design to represent our mountain-style (log furniture) and country-style (barnwood furniture) product line. We would like to re-create our existing homepage with a similar style template for our product line.
Our website is currently under construction – a draft has been published as an example outline. We are currently using Plinkora.example for our online store.
THEME
The overall theme needs to appear rustic, yet elegant. Listed below are only suggestions, not requirements. Please use your own creativity.
* Photographs: We will use our own photographs, for now any photograph will suffice.
* Background Colors: dark brown (rgb 21-9-2), medium brown (rgb 39-17-4), light brown (rgb 72-34-3). White background is also an option.
* Font Colors: beige (rgb 233-164-118), gold (rgb 151-98-2)
• Mountain-Style Images: cabin, wildlife, mountains, fishing, wildlife, trees, etc.
* Mountain-Style Colors: hunter green
* Country-Style Images: western, ranch, barn, farm animals, horse buggies, horseshoes, etc.
* Country-Style Colors: maroon
Thanks to all who are participating.
Target Market(s)
Outdoor enthusiasts who enjoy mountain living or country living. Our primary target market is our local market and within a 100 mile radius of our location.
Industry/Entity Type
Construction
Requirements
Must have
- Rustic, yet elegant design.
Homepage and product template page for displaying each item.
Nice to have
- Source code and functionality is optional.
Mountain-Style theme to represent our collection of log furniture and décor suited for cabins and lodges. Suggested color: hunter green. Images may include cabin, wildlife, mountains, fishing, wildlife, trees, etc.
Country-Style theme to represent our collection of barnwood furniture and décor suited for farms and ranches. Suggested color: maroon. Images may include western, ranch, barn, farm animals, horse buggies, horseshoes, etc.

```html
<!DOCTYPE html>
<html lang="en">
<head>
<meta charset="utf-8">
<title>Birch &amp; Ember Supply House</title>
<link rel="stylesheet" href="https://fonts.googleapis.com/css2?family=Arimo:wght@400;700&family=Oswald:wght@300;400&display=swap">
<style>
:root{
  --bg-dark:#150902;
  --bg-mid:#271104;
  --bg-light:#482203;
  --beige:#e9a476;
  --gold:#976202;
  --peach:#e8a27a;
  --white:#ffffff;
  --text-soft:#d9c3b0;
  --card:#1a0b03;
  --frame:#e6d8c8;
}
*{margin:0;padding:0;box-sizing:border-box}
html,body{width:806px;height:1200px;overflow:hidden}
body{
  position:relative;
  font-family:"Arimo",Arial,sans-serif;
  color:var(--white);
  background:
    repeating-linear-gradient(90deg,rgba(0,0,0,.35) 0 2px,transparent 2px 64px),
    linear-gradient(180deg,var(--bg-mid),var(--bg-dark) 40%,var(--bg-mid) 70%,var(--bg-dark));
}
.site-header{position:absolute;left:0;top:0;width:806px;height:160px}
.brand{
  position:absolute;left:331px;top:0;width:144px;height:110px;
  background:var(--bg-dark);
  display:flex;flex-direction:column;align-items:center;justify-content:center;gap:10px;
}
.brand-mark{width:18px;height:18px;background:var(--beige)}
.brand-name{font-weight:700;font-size:14px;color:var(--beige);letter-spacing:1px;text-transform:uppercase;white-space:nowrap}
.main-nav{position:absolute;left:108px;top:124px;width:586px;display:flex;justify-content:space-between;align-items:center}
.main-nav a{font-size:7.5px;color:var(--beige);text-decoration:none;text-transform:uppercase;white-space:nowrap;padding:6px 0}
.main-nav a.active{border:1px solid #6a4a35;padding:6px 5px;color:var(--white)}
.hero{
  position:absolute;left:0;top:160px;width:806px;height:346px;
  background:
    linear-gradient(180deg,rgba(0,0,0,0) 60%,rgba(120,20,15,.55) 78%,rgba(90,15,10,.7) 100%),
    linear-gradient(90deg,#6e3512 0%,#a0581f 22%,#8c4b1d 38%,#6d6559 52%,#5c5750 64%,#3a2a22 72%,#7d2c1a 86%,#5a2412 100%);
  border-bottom:3px solid var(--peach);
}
.hero-caption{position:absolute;left:112px;top:148px;padding:8px;background:rgba(40,18,6,.35)}
.hero-title{font-weight:700;font-size:27px;line-height:32px;color:var(--white);white-space:nowrap}
.hero-sub{margin-top:10px;font-size:12.5px;color:var(--white);white-space:nowrap}
.hero-arrows{position:absolute;left:373px;top:248px;display:flex;gap:4px}
.hero-arrows span{width:18px;height:18px;background:rgba(0,0,0,.6);display:flex;align-items:center;justify-content:center}
.intro{position:absolute;left:0;top:534px;width:806px;text-align:center}
.intro h1{font-family:"Oswald",sans-serif;font-weight:300;font-size:27px;color:var(--beige);letter-spacing:.5px}
.intro p{margin-top:12px;font-size:8.5px;line-height:16px;color:var(--text-soft)}
.product-grid{position:absolute;left:120px;top:638px;width:572px;display:grid;grid-template-columns:repeat(3,180px);column-gap:16px;row-gap:22px}
.product-card{height:190px;background:var(--card);text-align:center}
.product-photo{height:103px;border:3px solid var(--frame)}
.photo-cabin{background:linear-gradient(180deg,#2f4a2a 0%,#3d5e34 35%,#5a3424 55%,#3c4d30 80%,#5f7a3e 100%)}
.photo-bedroom{background:linear-gradient(180deg,#6e3e1e 0%,#b27a44 40%,#d7b48a 60%,#7a2a1e 85%,#5a2216 100%)}
.photo-lodge{background:linear-gradient(180deg,#5c3f28 0%,#a69684 35%,#e0dbd0 50%,#8c6448 70%,#5a2418 100%)}
.product-title{margin-top:13px;font-weight:700;font-size:13px;color:var(--white)}
.product-text{margin:8px 10px 0;font-size:7.5px;line-height:13px;color:var(--gold)}
.footer-nav{position:absolute;left:0;top:1080px;width:806px;height:31px;background:var(--peach)}
.footer-nav .links{position:absolute;left:114px;top:0;width:578px;height:31px;display:flex;justify-content:space-between;align-items:center}
.footer-nav a{font-size:7.5px;color:var(--bg-mid);text-decoration:none;text-transform:uppercase;white-space:nowrap}
.site-footer{position:absolute;left:0;top:1111px;width:806px;height:89px;background:var(--bg-dark);text-align:center}
.follow{margin-top:13px;font-size:8px;color:var(--white)}
.social{display:flex;justify-content:center;gap:4px;margin-top:6px}
.social span{width:17px;height:17px}
.social .s1{background:#3b5998}.social .s2{background:#3aa0d8}.social .s3{background:#2b7bb9}.social .s4{background:#6a8a3a}
.copyright{margin-top:6px;font-size:7.5px;line-height:12px;color:var(--white)}
</style>
</head>
<body>
<header class="site-header">
  <div class="brand">
    <span class="brand-mark"></span>
    <span class="brand-name">Birch &amp; Ember</span>
  </div>
  <nav class="main-nav">
    <a class="active" href="#">Home</a><a href="#">Online Store</a><a href="#">Bedroom</a><a href="#">Kitchen</a><a href="#">Living Room Office / Bar Room Outdoor</a><a href="#">Lighting</a><a href="#">Wall Decor</a><a href="#">Accessories</a><a href="#">About Us</a><a href="#">Contact Us</a>
  </nav>
</header>

<section class="hero" role="img" aria-label="Photo of a log lodge living room with stone fireplace, red armchairs and patterned rug">
  <div class="hero-caption">
    <h2 class="hero-title">Lorem ipsum dolor sit<br>amet, consectetur</h2>
    <p class="hero-sub">Lorem ipsum dolor sit amet, consectetur adipiscing elit</p>
  </div>
  <div class="hero-arrows">
    <span><svg width="8" height="10" viewBox="0 0 8 10"><path d="M6 1 2 5l4 4" fill="none" stroke="#fff" stroke-width="1.5"/></svg></span>
    <span><svg width="8" height="10" viewBox="0 0 8 10"><path d="M2 1l4 4-4 4" fill="none" stroke="#fff" stroke-width="1.5"/></svg></span>
  </div>
</section>

<section class="intro">
  <h1>RUSTIC / WESTERN FURNITURE &amp; ACCESSORIES</h1>
  <p>Lorem ipsum dolor sit amet, consectetur adipiscing elit, sed do eiusmod tempor incididunt ut labore et dolore magna aliqua.<br>Ut enim ad minim veniam, quis nostrud exercitation ullamco laboris nisi ut aliquip ex ea commodo consequat.</p>
</section>

<section class="product-grid">
  <article class="product-card"><div class="product-photo photo-cabin" role="img" aria-label="Photo of a log cabin among pine trees"></div><h3 class="product-title">Lorem ipsum dolor</h3><p class="product-text">Sed ut perspiciatis unde omnis iste natus error sit voluptatem accusantium doloremque.</p></article>
  <article class="product-card"><div class="product-photo photo-bedroom" role="img" aria-label="Photo of a log bed in a rustic bedroom"></div><h3 class="product-title">Lorem ipsum dolor</h3><p class="product-text">Sed ut perspiciatis unde omnis iste natus error sit voluptatem accusantium doloremque.</p></article>
  <article class="product-card"><div class="product-photo photo-lodge" role="img" aria-label="Photo of a lodge sitting room with antler chandelier"></div><h3 class="product-title">Lorem ipsum dolor</h3><p class="product-text">Sed ut perspiciatis unde omnis iste natus error sit voluptatem accusantium doloremque.</p></article>
  <article class="product-card"><div class="product-photo photo-cabin" role="img" aria-label="Photo of a log cabin among pine trees"></div><h3 class="product-title">Lorem ipsum dolor</h3><p class="product-text">Sed ut perspiciatis unde omnis iste natus error sit voluptatem accusantium doloremque.</p></article>
  <article class="product-card"><div class="product-photo photo-bedroom" role="img" aria-label="Photo of a log bed in a rustic bedroom"></div><h3 class="product-title">Lorem ipsum dolor</h3><p class="product-text">Sed ut perspiciatis unde omnis iste natus error sit voluptatem accusantium doloremque.</p></article>
  <article class="product-card"><div class="product-photo photo-lodge" role="img" aria-label="Photo of a lodge sitting room with antler chandelier"></div><h3 class="product-title">Lorem ipsum dolor</h3><p class="product-text">Sed ut perspiciatis unde omnis iste natus error sit voluptatem accusantium doloremque.</p></article>
</section>

<nav class="footer-nav">
  <div class="links"><a href="#">Home</a><a href="#">Online Store</a><a href="#">Bedroom</a><a href="#">Kitchen</a><a href="#">Living Room Office / Bar Room Outdoor</a><a href="#">Lighting</a><a href="#">Wall Decor</a><a href="#">Accessories</a><a href="#">About Us</a><a href="#">Contact Us</a></div>
</nav>

<footer class="site-footer">
  <p class="follow">Follow Us</p>
  <div class="social"><span class="s1"></span><span class="s2"></span><span class="s3"></span><span class="s4"></span></div>
  <p class="copyright">© 2014 Copyright Birch &amp; Ember Supply House<br>All Rights Reserved.</p>
</footer>
</body>
</html>
```